Flyer for the Radiant Harvest Worship Day

I am looking to create a flyer for a one day prayer retreat our church is organizing.
This flyer will be posted on social media, websites and will also be printed so it can be mailed to people.
I am looking for something professional, with good use of our logo and band colors (logo colors).
I am counting on the designer's skill, creativity, art and knowledge of media communication to produce a flyer that will effectively and quickly convey the message we are trying to spread.
CONTENT OF THE FLYER:
Event title: Radiant Harvest Worship Day
Date: Tuesday July 2nd, 2019
Time: 11:00AM - 7:00PM
Belmont Hotel, 4875 Maple Ridge Road, Portland, Maine 04219 (Room: Evergreen)
Event Key words to highlight what the event is about: Prayer, Sharing the Word, Panel discussion, prophecy, Impartation.
Key phrases:
A one day prayer retreat.
Jesus Chris is Lord
Contact info:
www.tuvela.org
Phone: 207 583 2194
Email: contact@brookmeadow.org

```html
<!DOCTYPE html>
<html lang="en">
<head>
<meta charset="utf-8">
<title>Radiant Harvest Worship Day – Flyer</title>
<link rel="stylesheet" href="https://fonts.googleapis.com/css2?family=Arimo:ital,wght@0,400;0,700;1,400;1,700&family=Libre+Baskerville:wght@700&display=swap">
<style>
  :root {
    --navy: #0e3a5c;
    --orange: #ef9226;
    --white: #ffffff;
    --paper: #ffffff;
    --hands-light: #f7f4ee;
  }
  * { margin: 0; padding: 0; box-sizing: border-box; }
  html, body {
    width: 1200px; height: 1200px; overflow: hidden;
    background: var(--paper);
    font-family: "Arimo", Arial, sans-serif;
  }
  .canvas { position: relative; width: 1200px; height: 1200px; }
  .size-label {
    position: absolute; top: 30px; left: 0; width: 1200px;
    text-align: center; color: var(--orange);
    font-family: "Libre Baskerville", Georgia, serif; font-weight: 700; font-size: 38px;
  }
  .flyer {
    position: absolute; left: 272px; top: 90px; width: 656px; height: 1020px;
    background: var(--navy); color: var(--white);
  }
  .flyer > * { position: absolute; }
  .event-title {
    left: 36px; top: 68px; color: var(--orange);
    font-family: "Libre Baskerville", Georgia, serif; font-weight: 700;
    font-size: 47px; line-height: 64px; letter-spacing: -0.5px;
  }
  .tagline { left: 38px; top: 198px; font-style: italic; font-size: 21px; }
  .event-date {
    left: 34px; top: 254px; height: 344px; width: 36px;
    writing-mode: vertical-rl; transform: rotate(180deg);
    font-weight: 700; font-style: italic; font-size: 27px; white-space: nowrap;
  }
  .rule-vertical { width: 4px; background: var(--orange); }
  .rule-date { left: 84px; top: 256px; height: 410px; }
  .event-details { left: 100px; top: 250px; font-weight: 700; font-size: 22px; line-height: 28px; }
  .hands-illustration { left: 396px; top: 226px; width: 188px; height: 356px; }
  .flame-decoration { left: 92px; top: 500px; width: 228px; height: 358px; }
  .keywords {
    right: 102px; top: 584px; text-align: right;
    font-size: 22px; line-height: 28px;
  }
  .rule-motto { left: 572px; top: 576px; height: 304px; }
  .motto {
    left: 584px; top: 580px; height: 298px; width: 36px;
    writing-mode: vertical-rl; transform: rotate(180deg);
    font-weight: 700; font-size: 29px; white-space: nowrap;
  }
  .contact { left: 39px; top: 884px; width: 240px; }
  .contact-heading {
    font-weight: 700; font-size: 18px; padding-bottom: 6px;
    border-bottom: 3px solid var(--orange); margin-bottom: 6px;
  }
  .contact-list { list-style: none; font-size: 16px; line-height: 20px; white-space: nowrap; }
  .org-mark { right: 42px; top: 912px; display: flex; align-items: center; gap: 10px; }
  .org-dot { width: 20px; height: 20px; border-radius: 50%; background: var(--orange); }
  .org-name {
    font-family: "Arimo", Arial, sans-serif; font-weight: 400; font-size: 40px;
    color: var(--white); letter-spacing: 1px;
  }
</style>
</head>
<body>
<div class="canvas">
  <div class="size-label">11 x 17</div>
  <main class="flyer">
    <h1 class="event-title">Radiant Harvest<br>Worship Day</h1>
    <p class="tagline">A one day prayer retreat.</p>

    <p class="event-date">Tuesday July 2nd, 2019</p>
    <div class="rule-vertical rule-date"></div>
    <p class="event-details">
      11:00AM - 7:00PM<br>
      Belmont Hotel,<br>
      4875 Maple Ridge Road,<br>
      Portland, Maine 04219<br>
      (Room: Evergreen)
    </p>

    <svg class="hands-illustration" role="img" aria-label="Illustration of praying hands holding a rosary with a cross" viewBox="0 0 188 356">
      <defs>
        <linearGradient id="handsTone" x1="0" y1="0" x2="0" y2="1">
          <stop offset="0" stop-color="#f7f4ee"/>
          <stop offset="1" stop-color="#f3c999"/>
        </linearGradient>
      </defs>
      <rect width="188" height="356" rx="10" fill="url(#handsTone)" opacity="0.9"/>
    </svg>

    <svg class="flame-decoration" role="img" aria-label="Large decorative flame area" viewBox="0 0 228 358">
      <rect width="228" height="358" rx="12" fill="var(--orange)" opacity="0.9"/>
    </svg>

    <p class="keywords">
      Prayer,<br>
      Sharing the Word,<br>
      Panel discussion,<br>
      prophecy,<br>
      Impartation.
    </p>
    <div class="rule-vertical rule-motto"></div>
    <p class="motto">Jesus Christ is Lord</p>

    <section class="contact">
      <h2 class="contact-heading">CONTACT US</h2>
      <ul class="contact-list">
        <li>Website: www.tuvela.org</li>
        <li>Phone: 207 583 2194</li>
        <li>Email: contact@brookmeadow.org</li>
      </ul>
    </section>

    <div class="org-mark">
      <span class="org-dot"></span>
      <span class="org-name">TUVELA</span>
    </div>
  </main>
</div>
</body>
</html>
```